Packaging design for a Deli Shop "TERU Gourmet"

We need a packaging design for a new Deli Business we are opening soon. We produce food to be packaged and sold either fresh or frozen in transparent disposable plastic boxes, cardboard boxes and finally delivered in a bag (Paper, plastic or shopping bag whatever goes best with the design) to take out. The food we generally pack are salads, lasagnas, ceviches, sandwiches, cookies, granola, dips, etc.

The name of the company is "TERU Gourmet" Check our website for reference: www.terugourmet-example.com

We have a logo and a name we want to maintain (attached).

The product will be sold in our new deli store, that is inspired in big cities delikatessen, quite modern and trendy. It also delivers a message that everything we sell is high quality, artisan (not massive or mainstream) and great in flavors.

Packaging must communicate freshness, great flavor, high quality and high price.

Packaging must be feasible to produce and print easily without any complex or impossible to implement packaging, (preferrable to be done or easy to adapt from generic packaging).

All our communication will be in Spanish so please do not depend on english for the design. If english or any other language is used, please be sure its understandable in almost any country (ie Basic English, Italian).

Same packaging (labeling or boxes and bags) will be used, just changing the name of the product inside according to the product.

Most of our product will be displayed in refrigerators and freezers.
Updates

I just uploaded a visual brief of the packaging examples we would like to have.

Looking forward to see your designs.
Thank you

Reason: Some designers who said will participate havent submitted their deaigns, and still what is being submitted is not fully complying with the requirements. Thank you

Target Market(s)

The main target is High SEL, between 24 and 40, mostly woman

Industry/Entity Type

Communication

Requirements
Must have

Nice to have
• Please take a look at my website www.terugourmet-example.com to see the kind of coloring we are aiming to have.

Give the impression of being "Green"...

Include "Kraft" color paper / Brown paper color
Should not have
• Complex packaging difficult to implement in a simple print shop.
Expensive items.

```html
<!DOCTYPE html>
<html lang="es">
<head>
<meta charset="utf-8">
<title>TERU Gourmet – fajillas, empaque y bolsa</title>
<link rel="stylesheet" href="https://fonts.googleapis.com/css2?family=Josefin+Sans:wght@400&family=Caveat:wght@400&family=Arimo:wght@400&display=swap">
<style>
  :root {
    --red: #e41e1e;
    --red-light: #f0241c;
    --red-dark: #c8141a;
    --wine: #8c0a18;
    --wine-light: #9a1020;
    --wine-dark: #650712;
    --orange: #fb7a10;
    --orange-light: #fb8a14;
    --orange-dark: #e0620c;
    --amber-light: #f8a232;
    --amber-dark: #d8700e;
    --green: #15b22f;
    --green-dark: #0f9a27;
    --kraft: #e4b394;
    --white: #ffffff;
    --label: #444444;
    --bg-center: #ffffff;
    --bg-edge: #dcdcdc;
  }
  * { box-sizing: border-box; margin: 0; padding: 0; }
  html, body { width: 1200px; height: 922px; overflow: hidden; }
  body {
    position: relative;
    background: radial-gradient(ellipse at 52% 52%, var(--bg-center) 0%, #f1f1f1 40%, var(--bg-edge) 100%);
    font-family: "Arimo", sans-serif;
  }
  .board-label {
    position: absolute;
    font-size: 12px;
    color: var(--label);
    letter-spacing: -0.2px;
  }
  .piece { position: absolute; }
  .panel { position: absolute; }

  /* soft tonal fields standing in for the woven wave pattern */
  .pattern-red {
    background:
      radial-gradient(ellipse 60% 45% at 30% 30%, rgba(200,20,26,0.55), transparent 70%),
      radial-gradient(ellipse 60% 45% at 70% 70%, rgba(200,20,26,0.55), transparent 70%),
      linear-gradient(135deg, var(--red-light), var(--red) 50%, var(--red-dark));
  }
  .pattern-orange-bright {
    background:
      radial-gradient(ellipse 55% 50% at 25% 35%, rgba(224,98,12,0.6), transparent 70%),
      radial-gradient(ellipse 55% 50% at 75% 65%, rgba(224,98,12,0.6), transparent 70%),
      linear-gradient(135deg, var(--orange-light), var(--orange) 50%, var(--orange-dark));
  }
  .pattern-orange {
    background:
      radial-gradient(ellipse 60% 40% at 30% 30%, rgba(216,112,14,0.6), transparent 70%),
      radial-gradient(ellipse 60% 40% at 70% 72%, rgba(216,112,14,0.6), transparent 70%),
      linear-gradient(160deg, var(--amber-light), #f29020 50%, var(--amber-dark));
  }
  .pattern-wine {
    background:
      radial-gradient(ellipse 60% 35% at 40% 25%, rgba(101,7,18,0.7), transparent 70%),
      radial-gradient(ellipse 60% 35% at 60% 75%, rgba(101,7,18,0.7), transparent 70%),
      linear-gradient(160deg, var(--wine-light), var(--wine) 50%, var(--wine-dark));
  }

  .flavor {
    position: absolute;
    font-family: "Caveat", cursive;
    color: var(--white);
    text-align: center;
    line-height: 0.95;
  }

  .brand {
    position: absolute;
    display: flex;
    flex-direction: column;
    align-items: center;
    justify-content: center;
    font-family: "Josefin Sans", sans-serif;
    font-weight: 400;
    color: var(--red);
    background: var(--white);
    line-height: 1;
  }
  .brand__name { letter-spacing: 1px; }
  .brand__tag { letter-spacing: 0.55em; margin-right: -0.55em; }

  /* vertical band */
  .band-vertical { left: 26px; top: 36px; width: 174px; height: 874px; }
  .band-vertical .top { left: 0; top: 0; width: 174px; height: 286px; }
  .band-vertical .flavor-panel { left: 0; top: 286px; width: 174px; height: 158px; background: var(--green); }
  .band-vertical .flavor { left: 0; right: 0; top: 102px; font-size: 27px; }
  .band-vertical .brand { left: 0; top: 444px; width: 174px; height: 144px; }
  .band-vertical .brand__name { font-size: 66px; }
  .band-vertical .brand__tag { font-size: 18px; margin-top: 8px; }
  .band-vertical .bottom { left: 2px; top: 588px; width: 172px; height: 286px; }

  /* horizontal band */
  .band-horizontal { left: 300px; top: 164px; width: 890px; height: 173px; }
  .band-horizontal .left { left: 0; top: 0; width: 283px; height: 173px; }
  .band-horizontal .brand { left: 283px; top: 0; width: 171px; height: 173px; }
  .band-horizontal .brand__name { font-size: 68px; }
  .band-horizontal .brand__tag { font-size: 18px; margin-top: 8px; }
  .band-horizontal .flavor-panel { left: 454px; top: 0; width: 154px; height: 173px; background: var(--wine); }
  .band-horizontal .flavor { left: 0; right: 0; top: 122px; font-size: 28px; }
  .band-horizontal .right { left: 608px; top: 0; width: 282px; height: 173px; }

  /* sandwich sleeve */
  .sleeve { left: 354px; top: 507px; width: 110px; height: 337px; background: var(--orange); }
  .sleeve .stripe { left: 25px; top: 0; width: 59px; height: 269px; background: var(--white); }
  .sleeve .flavor-panel { left: 9px; top: 0; width: 92px; height: 104px; background: var(--red); }
  .sleeve .flavor { left: 0; right: 0; top: 58px; font-size: 18px; }
  .sleeve .brand { left: 0; top: 269px; width: 110px; height: 68px; }
  .sleeve .brand__name { font-size: 28px; }
  .sleeve .brand__tag { font-size: 7px; margin-top: 4px; }

  .wedge { left: 543px; top: 514px; width: 169px; height: 332px; }

  /* bag */
  .bag { left: 907px; top: 440px; width: 255px; height: 394px; }
  .bag .handle { left: 0; top: 0; width: 255px; height: 100px; }
  .bag .front { left: 0; top: 72px; width: 136px; height: 322px; background: var(--kraft); }
  .bag .side { left: 136px; top: 72px; width: 119px; height: 322px; }
  .bag .brand { left: 18px; top: 290px; width: 100px; height: 80px; background: transparent; }
  .bag .brand__name { font-size: 42px; }
  .bag .brand__tag { font-size: 11px; margin-top: 6px; }
</style>
</head>
<body>

  <p class="board-label" style="left:76px; top:18px;">fajilla vertical</p>
  <section class="piece band-vertical">
    <div class="panel top pattern-red" role="img" aria-label="Patrón de ondas entrelazadas en tonos rojos"></div>
    <div class="panel flavor-panel">
      <p class="flavor">risoni<br>mediterranea</p>
    </div>
    <div class="brand"><span class="brand__name">TERU</span><span class="brand__tag">GOURMET</span></div>
    <div class="panel bottom pattern-orange" role="img" aria-label="Patrón de ondas entrelazadas en tonos naranjas"></div>
  </section>

  <p class="board-label" style="left:306px; top:139px;">fajilla horizontal</p>
  <section class="piece band-horizontal">
    <div class="panel left pattern-orange-bright" role="img" aria-label="Patrón de ondas entrelazadas en tonos naranjas"></div>
    <div class="brand"><span class="brand__name">TERU</span><span class="brand__tag">GOURMET</span></div>
    <div class="panel flavor-panel">
      <p class="flavor">brownies</p>
    </div>
    <div class="panel right pattern-red" role="img" aria-label="Patrón de ondas entrelazadas en tonos rojos"></div>
  </section>

  <p class="board-label" style="left:356px; top:488px;">empaque sandwiches</p>
  <section class="piece sleeve">
    <div class="panel stripe"></div>
    <div class="panel flavor-panel">
      <p class="flavor">pavo con<br>manchego</p>
    </div>
    <div class="brand"><span class="brand__name">TERU</span><span class="brand__tag">GOURMET</span></div>
  </section>

  <svg class="piece wedge" viewBox="0 0 169 332" role="img" aria-label="Triángulo de empaque con patrón de ondas en tonos verdes">
    <defs>
      <linearGradient id="wedge-fill" x1="0" y1="0" x2="0" y2="1">
        <stop offset="0" stop-color="#1bb533"/>
        <stop offset="0.3" stop-color="#12a42b"/>
        <stop offset="0.5" stop-color="#1bb533"/>
        <stop offset="0.75" stop-color="#0f9a27"/>
        <stop offset="1" stop-color="#1bb533"/>
      </linearGradient>
    </defs>
    <polygon points="0,0 0,332 169,332" fill="url(#wedge-fill)"/>
  </svg>

  <section class="piece bag">
    <svg class="panel handle" viewBox="0 0 255 100" aria-hidden="true">
      <path d="M49 88 C 49 20, 200 20, 200 88" fill="none" stroke="#8c0a18" stroke-width="3"/>
    </svg>
    <div class="panel front"></div>
    <div class="panel side pattern-wine" role="img" aria-label="Patrón de ondas entrelazadas en tonos vino"></div>
    <svg class="panel" style="left:0; top:0; width:255px; height:100px;" viewBox="0 0 255 100" aria-hidden="true">
      <circle cx="49" cy="88" r="6" fill="#ffffff"/>
      <circle cx="200" cy="88" r="6" fill="#ffffff"/>
    </svg>
    <div class="brand"><span class="brand__name">TERU</span><span class="brand__tag">GOURMET</span></div>
  </section>

</body>
</html>
```